New modern website for Kerbline Groundworks

Hi we are an existing company that has a current website http://www.kerblinegroundworks.co.nz/ we are looking to get a new vibrant looking website designed to take us further and gain more customers. We are after a simple easy to use website that does not confuse but we want to make an impact and stand out from the rest

Target Market(s)

Homeowners And Commercial Businesses

Industry/Entity Type

It Company

Coding

Coded - Design and coding required

Number of Pages Required

2 page

```html
<!DOCTYPE html>
<html lang="en">
<head>
<meta charset="utf-8">
<title>Kerbline Groundworks</title>
<link href="https://fonts.googleapis.com/css2?family=Montserrat:wght@400;600;700;800&family=Open+Sans:wght@400;600&display=swap" rel="stylesheet">
<style>
:root{
  --yellow:#f3e81c;
  --yellow-deep:#e8d800;
  --dark:#262626;
  --darker:#1b1b1b;
  --ink:#2c2c2c;
  --muted:#8a8a8a;
  --line:#e4e4e4;
  --paper:#ffffff;
  --soft:#f6f6f6;
}
*{box-sizing:border-box;margin:0;padding:0}
html,body{width:1200px;height:2488px;overflow:hidden;background:var(--paper)}
body{font-family:"Open Sans",Arial,sans-serif;color:var(--ink);font-size:11px;line-height:1.6;position:relative}
h1,h2,h3,h4,.nav,.btn{font-family:"Montserrat",Arial,sans-serif}
.wrap{position:absolute;left:240px;width:720px}
.ph{display:block}
a{color:inherit;text-decoration:none}

/* header + hero */
.hero{position:absolute;top:0;left:0;width:1200px;height:420px;
  background:linear-gradient(160deg,#6f8fb0 0%,#9fb4c6 35%,#c0733a 55%,#d9642a 62%,#7b8590 80%,#596270 100%)}
.topbar{position:absolute;top:0;left:0;width:1200px;height:80px;background:rgba(20,20,20,.72)}
.logo{position:absolute;left:240px;top:22px;display:flex;align-items:center;gap:8px;color:#fff;font-family:"Montserrat",sans-serif;font-weight:700;font-size:16px;letter-spacing:.5px}
.logo .mark{width:14px;height:14px;background:var(--yellow)}
.phone{position:absolute;right:240px;top:10px;color:#ddd;font-size:10px}
.phone b{color:var(--yellow)}
.nav{position:absolute;right:240px;top:44px;display:flex;gap:26px;font-size:10px;color:#eee;font-weight:600}
.nav .on{color:var(--yellow)}

/* features */
.features{top:352px;display:flex;gap:30px}
.feature{width:220px}
.feature .ph{height:118px;background:linear-gradient(135deg,#c9a34a,#7c6a55)}
.feature:nth-child(2) .ph{background:linear-gradient(135deg,#8aa0b5,#5b4a3b)}
.feature:nth-child(3) .ph{background:linear-gradient(135deg,#a6b6c2,#6e7a52)}
.feature h3{font-size:12px;margin:16px 0 6px;font-weight:700}
.feature p{color:var(--muted);font-size:9.5px}
.more{display:inline-block;margin-top:8px;font-size:9px;color:#b8a800;font-weight:600}

/* banner */
.banner{position:absolute;top:608px;left:0;width:1200px;height:320px;
  background:linear-gradient(90deg,#8d9095 0%,#b8bbbf 45%,#e1ddd4 70%,#d7c8ad 100%)}
.banner .ph{position:absolute;right:0;top:0;width:520px;height:320px;background:linear-gradient(100deg,rgba(225,221,212,0) 0%,#cbb894 40%,#8c8478 100%)}
.banner .txt{position:absolute;left:240px;top:92px;color:#fff}
.banner small{font-size:10px;font-weight:600}
.banner h1{font-size:26px;line-height:1.25;font-weight:800;text-transform:uppercase;margin:6px 0 16px;letter-spacing:.5px}
.btn{display:inline-block;border:1px solid #fff;padding:6px 14px;font-size:9px;font-weight:600;color:#fff}

/* section titles */
.stitle{display:flex;justify-content:space-between;align-items:center;border-bottom:1px solid var(--line);padding-bottom:8px}
.stitle h2{font-size:15px;font-weight:700}
.arrows{display:flex;gap:4px}
.arrows span{width:14px;height:14px;background:#eee;display:block}
.arrows.yellow span{background:var(--yellow)}

/* what we do */
.what{top:968px}
.cards{display:flex;gap:30px;margin-top:22px}
.card{width:220px}
.card .ph{height:96px;background:linear-gradient(135deg,#9db0c4,#6d5d4d)}
.card:nth-child(2) .ph{background:linear-gradient(135deg,#a0b6cf,#c9682e)}
.card:nth-child(3) .ph{background:linear-gradient(135deg,#d8dde2,#6f7d8c)}
.card h3{font-size:12px;margin:14px 0 6px;font-weight:700}
.card p{color:var(--muted);font-size:9.5px}

/* services */
.services{position:absolute;top:1300px;left:0;width:1200px;height:300px;background:var(--dark)}
.services .stitle{border-color:#444}
.services h2{color:#fff}
.boxes{display:flex;gap:30px;margin-top:34px}
.box{width:220px;height:168px;background:var(--yellow);border:1px solid var(--yellow-deep);padding:24px 20px;text-align:center}
.box h3{font-size:12px;font-weight:800;margin-bottom:8px}
.box p{font-size:9px;color:#4a4620}

/* projects */
.projects{top:1628px}
.project{width:220px}
.project .ph{height:100px;background:linear-gradient(135deg,#8fb0d4,#4a5f3c)}
.project:nth-child(2) .ph{background:linear-gradient(135deg,#b7c4d1,#a87f52)}
.project:nth-child(3) .ph{background:linear-gradient(135deg,#9a6d5a,#2f3442)}
.project h3{font-size:11px;margin:14px 0 6px;font-weight:700}
.meta{display:flex;justify-content:space-between;font-size:8px;color:var(--muted);border-top:1px solid var(--line);border-bottom:1px solid var(--line);padding:3px 0;margin-bottom:8px}
.project p{color:var(--muted);font-size:9.5px}
.ghost{display:inline-block;margin-top:10px;border:1px solid #ccc;padding:3px 10px;font-size:8px;color:#777}

/* clients + testimonials */
.lower{top:2008px;display:flex;gap:60px}
.clients{width:300px}
.testi{width:360px}
.lower h2{font-size:15px;font-weight:700;margin-bottom:24px}
.clogos{display:grid;grid-template-columns:repeat(3,1fr);gap:22px 10px}
.clogo{display:flex;align-items:center;gap:5px;font-size:9px;font-weight:600;color:#888}
.clogo i{width:10px;height:10px;background:#bbb;display:block}
.social{margin-top:48px;width:180px;height:28px;background:var(--yellow);display:flex;align-items:center;gap:6px;padding-left:10px}
.social span{width:12px;height:12px;border-radius:50%;background:var(--dark);display:block}
.testi p{font-size:9.5px;color:var(--muted);font-style:italic}
.author{display:flex;align-items:center;gap:12px;margin-top:18px}
.author .ph{width:40px;height:40px;border-radius:50%;background:linear-gradient(135deg,#c9b8a6,#6b5d52)}
.author b{font-size:10px;display:block}
.author small{font-size:8.5px;color:var(--muted)}

/* footer */
.footer{position:absolute;top:2352px;left:0;width:1200px;height:96px;background:var(--dark);color:#aaa}
.fcols{top:14px;display:flex;gap:30px}
.fcol{width:160px;font-size:8px;line-height:1.55}
.fcol h4{color:#fff;font-size:9px;font-weight:700;margin-bottom:6px;text-transform:uppercase}
.fcol.links{width:120px}
.bottom{position:absolute;top:2448px;left:0;width:1200px;height:40px;background:var(--darker);color:#888;font-size:8.5px}
.bottom .wrap{top:13px;display:flex;justify-content:space-between}
.bottom nav{display:flex;gap:14px}
</style>
</head>
<body>

<header class="hero">
  <div class="ph" role="img" aria-label="Photo of an orange excavator working on a construction site" style="position:absolute;inset:0"></div>
  <div class="topbar">
    <div class="logo"><span class="mark"></span>Kerbline Groundworks</div>
    <div class="phone">Call us: <b>09 555 0142</b></div>
    <nav class="nav"><a class="on">Home</a><a>Company</a><a>Recent Work</a><a>Services</a><a>Our Clients</a><a>Careers</a><a>Contact Us</a></nav>
  </div>
</header>

<section class="wrap features">
  <article class="feature"><div class="ph" role="img" aria-label="Photo of a site worker in a hard hat"></div><h3>Our expertise</h3><p>Decades of groundwork experience across residential and commercial sites, delivered safely, on time and on budget.</p><a class="more">Read more</a></article>
  <article class="feature"><div class="ph" role="img" aria-label="Photo of fresh asphalt being laid"></div><h3>Excavating &amp; Asphalt Work</h3><p>Driveways, car parks and roads prepared, laid and finished by our own crews with modern plant and machinery.</p><a class="more">Read more</a></article>
  <article class="feature"><div class="ph" role="img" aria-label="Photo of a finished house with new driveway"></div><h3>Additional Services</h3><p>Drainage, kerbing, retaining and site clearing, so one team can handle your whole project from start to finish.</p><a class="more">Read more</a></article>
</section>

<section class="banner">
  <div class="ph" role="img" aria-label="Photo of a smiling contractor holding a cordless drill"></div>
  <div class="txt">
    <small>Welcome Info is</small>
    <h1>Contractors &amp; Construction<br>Managers Since 1989</h1>
    <a class="btn">Get a Quote</a>
  </div>
</section>

<section class="wrap what">
  <div class="stitle"><h2>What We Do</h2><div class="arrows"><span></span><span></span></div></div>
  <div class="cards">
    <article class="card"><div class="ph" role="img" aria-label="Photo of a roofer at work"></div><h3>Metal Roofing</h3><p>Durable metal roofing installed to last, with careful detailing and clean finishes on every job we take on.</p><a class="more">Read more</a></article>
    <article class="card"><div class="ph" role="img" aria-label="Photo of an excavator digging"></div><h3>General Contracting</h3><p>Full site management and earthworks for builds of any size, coordinated by one experienced project team.</p><a class="more">Read more</a></article>
    <article class="card"><div class="ph" role="img" aria-label="Photo of consultants reviewing plans"></div><h3>Construction Consultant</h3><p>Practical advice on planning, consents and costs so your project starts right and stays on track throughout.</p><a class="more">Read more</a></article>
  </div>
</section>

<section class="services">
  <div class="wrap" style="top:36px">
    <div class="stitle"><h2>Services</h2><div class="arrows yellow"><span></span><span></span></div></div>
    <div class="boxes">
      <div class="box"><h3>SERVICE 1</h3><p>Site preparation, excavation and levelling for new homes and commercial builds.</p></div>
      <div class="box"><h3>SERVICE 2</h3><p>Asphalt driveways, car parks and access roads laid to a smooth lasting finish.</p></div>
      <div class="box"><h3>SERVICE 3</h3><p>Kerbing, channels and stormwater drainage built to council standards.</p></div>
    </div>
  </div>
</section>

<section class="wrap projects">
  <div class="stitle"><h2>Recent Projects</h2><div class="arrows"><span></span><span></span></div></div>
  <div class="cards">
    <article class="project"><div class="ph" role="img" aria-label="Photo of a finished family home"></div><h3>Finding New Building In the Sun</h3><div class="meta"><span>12 March 2024</span><span>Residential</span></div><p>New driveway, paths and drainage completed for a family home build in the suburbs.</p><a class="ghost">Read more</a></article>
    <article class="project"><div class="ph" role="img" aria-label="Photo of timber framing on a new build"></div><h3>How To Build A Construction Plan</h3><div class="meta"><span>28 Feb 2024</span><span>Commercial</span></div><p>Earthworks and services trenching for a new two storey commercial building.</p><a class="ghost">Read more</a></article>
    <article class="project"><div class="ph" role="img" aria-label="Photo of a team group at a site opening"></div><h3>Construction Honored with ISO Builders</h3><div class="meta"><span>10 Feb 2024</span><span>News</span></div><p>Our crew recognised for safety and quality across a year of major projects.</p><a class="ghost">Read more</a></article>
  </div>
</section>

<section class="wrap lower">
  <div class="clients">
    <h2>Our Clients</h2>
    <div class="clogos">
      <div class="clogo"><i></i>Northgate</div>
      <div class="clogo"><i></i>Ridgeway</div>
      <div class="clogo"><i></i>Harbourline</div>
      <div class="clogo"><i></i>Tessera</div>
      <div class="clogo"><i></i>Alderbuild</div>
      <div class="clogo"><i></i>Copperfield</div>
    </div>
    <div class="social"><span></span><span></span><span></span><span></span><span></span></div>
  </div>
  <div class="testi">
    <h2>Testimonials</h2>
    <p>"The crew turned up when they said they would, kept the site tidy and left us with a driveway we are proud of. Clear pricing, no surprises and a finish that has held up through every winter since. We will use them again."</p>
    <div class="author"><div class="ph" role="img" aria-label="Portrait of the client"></div><div><b>Marcus Hale</b><small>Homeowner</small></div></div>
  </div>
</section>

<footer class="footer">
  <div class="wrap fcols">
    <div class="fcol"><h4>About Company</h4>Local groundworks specialists serving homeowners and businesses with quality asphalt, kerbing and civil work since 1989.</div>
    <div class="fcol links"><h4>Company</h4>Home<br>About Us<br>Services<br>Careers</div>
    <div class="fcol"><h4>Construction Office</h4>48 Quarry Road, Penrose, Auckland<br>09 555 0142<br>hello@kerblinegroundworks.co.nz</div>
    <div class="fcol"><h4>Business Hours</h4>Mon – Fri: 7am – 5pm<br>Saturday: 8am – 12pm<br>Sunday: Closed</div>
  </div>
</footer>
<div class="bottom">
  <div class="wrap"><span>© 2024 Kerbline Groundworks. All rights reserved.</span><nav><a>Services</a><a>Clients</a><a>Contact</a><a>Privacy</a></nav></div>
</div>

</body>
</html>
```